VarnoBud CBD Tincture packaging design

We are seeking a designer to create the label that will be printed on cardboard box packaging, which will carry our CBD tincture. We envision the box being white to resemble a clean look that stands out on shelves. Our logo (attached) uses shades of yellows and greens in the form of a fluid drop resembling half plant and half plant extract. The packaging will show that we only use clean (TRELK certified) hemp extract thats been extracted using the cleanest method of extraction; supercritical CO2. Our tincture uses a fractionated coconut oil to improve absorption for the consumer, increasing onset time and providing essential omega fatty acids. We take pride in our use of a clean product with a clean extraction. The tincture bottle itself holds 30ml of liquid and is a clear glass bottle. The cap for the tincture bottle is white and has a graduated glass stem that shows the measurements for how much liquid it holds (picture attached). We have not yet done the label that will stick on the tincture, but i image it will be a frosted white label with the VarnoBud logo and a few words describing the product. This project is for the cardboard box that will hold each individual tincture bottle.

BOX DIMENSIONS: 1.31" x 1.31" x 4.13" (LxWxH)

We will be releasing a new product (cbd capsules) in April, and we will reach out to the designer of this product as first option to create the design for the capsule packaging.

Target Market(s)

convenience stores, medical marijuana dispensaries, health stores

Font styles to use
Serif

Colors
ffffff
fbed22
ffc214
ffcf3e
acd136
9bcb3c

Requirements
Must have
• -VarnoBud company logo
-Made with full spectrum supercritical CO2 Hemp Extract
-Made from TRELK certified clean hemp
-Declaration of ingredients (fractionated coconut oil, CBD hemp extract)
-1200mg CBD Tincture
-Nt. Wt. 1FL OZ (30ml)
-These statements have not been evaluated by the Bureau of Remedy Oversight. BRO has not evaluated this product for safety or efficacy. This product is not intended to diagnose, treat, cure or prevent any disease.
-DO NOT REFRIGERATE. Keep at room temperature to preserve freshness. Store away from humidity, heat, and light. Warning: If pregnant, nursing or taking prescription drugs, consult your physician prior to use. Keep out of reach of children.
-Manufactured by VarnoBud CBD Co. 58 Corrow Bend Ln. Brenmoor, VT 04091
-Batch ID:___________
-Expiration Date:____________
-Good Manufacturing Practice (GMP) Logo
-TRELK logo
Nice to have
• -Contains omega 3, 6 and essential fatty acids
-Graduated dropper for precise dosing
-40mg of CBD per dropper!
-Made in the USA
-No Pesticides
-No Solvents
-No Heavy Metals
-CO2 Extraction
-3rd Party Lab Tested

```html
<!DOCTYPE html>
<html lang="en">
<head>
<meta charset="utf-8">
<title>VarnoBud CBD Tincture – box dieline</title>
<link href="https://fonts.googleapis.com/css2?family=Oswald:wght@500;700&family=Roboto+Condensed:wght@400;700&display=swap" rel="stylesheet">
<style>
  :root {
    --white: #ffffff;
    --page: #e9ede4;
    --yellow: #fbed22;
    --gold: #ffc214;
    --lime: #acd136;
    --leaf: #9bcb3c;
    --forest: #3f9a2a;
    --deep: #0d5a2a;
    --ink: #1d2618;
    --alert: #e5232a;
  }
  * { margin: 0; padding: 0; box-sizing: border-box; }
  html, body { width: 1200px; height: 531px; overflow: hidden; }
  body {
    background: var(--page);
    font-family: "Roboto Condensed", sans-serif;
    color: var(--ink);
    position: relative;
  }
  .dieline { position: absolute; left: 285px; top: 15px; width: 630px; height: 501px; }
  .glue-flap { position: absolute; left: 0; top: 142px; width: 46px; height: 359px; background: var(--white); box-shadow: 0 0 0 0.5px #cfd4c8; }
  .top-flap {
    position: absolute; left: 46px; top: 0; width: 145px; height: 142px;
    background: var(--white); box-shadow: 0 0 0 0.5px #cfd4c8;
    display: flex; flex-direction: column; align-items: center; justify-content: center;
    transform: rotate(180deg);
  }
  .top-flap .brand-name { font-size: 10px; color: var(--deep); margin-bottom: 2px; }
  .top-flap .flap-title { font-family: "Oswald", sans-serif; font-weight: 700; font-size: 22px; color: var(--deep); line-height: 1; }
  .top-flap .flap-dose { font-family: "Oswald", sans-serif; font-weight: 500; font-size: 14px; color: var(--deep); line-height: 1.3; }

  .panel-strip { position: absolute; left: 46px; top: 142px; width: 584px; height: 359px; background: var(--white); overflow: hidden; }
  .waves { position: absolute; inset: 0; }
  .panel { position: absolute; top: 0; height: 359px; }
  .panel--icons { left: 0; width: 166px; }
  .panel--front { width: 124px; text-align: center; }
  .panel--front.one { left: 166px; }
  .panel--front.two { left: 460px; }
  .panel--info { left: 290px; width: 170px; }

  .brand-block {
    position: absolute; left: 3px; top: 0; width: 98px; height: 171px;
    background: var(--lime);
    display: flex; flex-direction: column; align-items: center;
  }
  .brand-name { font-family: "Roboto Condensed", sans-serif; font-weight: 400; color: var(--deep); }
  .brand-block .brand-name { font-size: 12px; margin-top: 50px; }
  .cbd { font-family: "Oswald", sans-serif; font-weight: 700; font-size: 60px; line-height: 1; color: var(--deep); margin-top: 6px; letter-spacing: 1px; }
  .tincture { font-family: "Oswald", sans-serif; font-weight: 700; font-size: 25px; line-height: 1; color: var(--deep); margin-top: 2px; }
  .front-body { position: absolute; left: 0; top: 176px; width: 104px; display: flex; flex-direction: column; align-items: center; }
  .dose { font-family: "Oswald", sans-serif; font-weight: 500; font-size: 13px; color: var(--deep); }
  .extract { font-size: 8.5px; line-height: 11px; margin-top: 8px; text-transform: uppercase; }
  .cert-badge { width: 46px; height: 46px; border-radius: 50%; background: var(--forest); margin-top: 12px; }
  .cert-note { font-family: "Oswald", sans-serif; font-weight: 500; font-size: 5.5px; line-height: 8px; color: var(--deep); margin-top: 5px; }
  .net { font-family: "Oswald", sans-serif; font-weight: 500; font-size: 5.5px; color: var(--deep); margin-top: 10px; }
  .volume { font-family: "Oswald", sans-serif; font-weight: 500; font-size: 9.5px; color: var(--deep); }

  .claims { position: absolute; left: 13px; top: 56px; width: 116px; display: grid; grid-template-columns: 1fr 1fr; row-gap: 2px; }
  .claim { display: flex; flex-direction: column; align-items: center; text-align: center; font-size: 7px; line-height: 9px; height: 60px; white-space: nowrap; }
  .claim svg { width: 36px; height: 36px; margin-bottom: 2px; }
  .batch { position: absolute; left: 15px; top: 311px; font-size: 7px; line-height: 14px; }

  .notes { position: absolute; left: 16px; top: 45px; width: 118px; font-size: 7px; line-height: 9.6px; text-align: justify; }
  .notes p { margin-bottom: 8px; }
  .ingredients { position: absolute; left: 16px; top: 192px; width: 118px; font-size: 7px; line-height: 9.6px; text-align: center; }
  .badges { position: absolute; left: 20px; top: 236px; width: 120px; display: flex; justify-content: space-between; }
  .badge { width: 45px; height: 45px; border-radius: 50%; background: var(--forest); }
  .maker { position: absolute; left: 22px; top: 299px; display: flex; align-items: flex-end; gap: 4px; }
  .maker .brand-name { font-size: 10px; }
  .maker address { font-style: normal; font-size: 7px; line-height: 9.6px; }
  .origin { position: absolute; left: 0; width: 160px; top: 338px; text-align: center; font-weight: 700; font-size: 7px; color: var(--deep); }
</style>
</head>
<body>
<main class="dieline">
  <div class="glue-flap"></div>

  <div class="top-flap">
    <span class="brand-name">VarnoBud</span>
    <span class="flap-title">CBD TINCTURE</span>
    <span class="flap-dose">1200MG</span>
  </div>

  <section class="panel-strip">
    <svg class="waves" viewBox="0 0 584 359" preserveAspectRatio="none" aria-hidden="true">
      <rect x="0" y="0" width="584" height="90" fill="#fbed22"/>
      <path d="M0 0H584V70C540 58 500 80 450 72S360 52 300 66 200 80 140 68 40 58 0 70Z" fill="#acd136"/>
      <path d="M0 0H584V46C530 36 490 56 440 48S350 30 290 42 190 56 130 44 40 34 0 46Z" fill="#9bcb3c"/>
      <path d="M0 0H584V22C540 14 500 30 450 24S360 10 300 18 200 30 140 20 40 12 0 22Z" fill="#3f9a2a"/>
      <path d="M0 90C50 80 110 104 170 92S280 76 340 88 460 102 584 86V100H0Z" fill="#ffffff"/>
      <path d="M0 306C60 296 120 318 190 306S320 288 400 300 520 316 584 300V359H0Z" fill="#fbed22"/>
      <path d="M0 326C70 318 140 336 210 328S340 312 420 322 530 334 584 322V359H0Z" fill="#ffcf3e" opacity="0.45"/>
    </svg>

    <div class="panel panel--icons">
      <div class="claims">
        <div class="claim">
          <svg viewBox="0 0 36 36"><circle cx="18" cy="18" r="16" fill="#fff" stroke="#0d5a2a" stroke-width="3"/><path d="M15 9C12 15 10 18 10 21a5 5 0 0 0 10 0c0-3-2-6-5-12Z" fill="#0d5a2a"/><path d="M23 14C21 18 20 20 20 22a3.5 3.5 0 0 0 7 0c0-2-1.5-4-4-8Z" fill="#0d5a2a"/></svg>
          Contains<br>Omega 3, 6
        </div>
        <div class="claim">
          <svg viewBox="0 0 36 36"><circle cx="18" cy="18" r="16" fill="#fff" stroke="#0d5a2a" stroke-width="3"/><path d="M14 12C11 18 9 21 9 23a5 5 0 0 0 10 0c0-2-2-5-5-11Z" fill="#0d5a2a"/><circle cx="23" cy="12" r="3" fill="#0d5a2a"/><circle cx="24" cy="21" r="3" fill="#0d5a2a"/></svg>
          Essential<br>Fatty Acids
        </div>
        <div class="claim">
          <svg viewBox="0 0 36 36"><circle cx="18" cy="18" r="16" fill="#fff" stroke="#0d5a2a" stroke-width="3"/><rect x="16" y="5" width="4" height="18" fill="none" stroke="#0d5a2a" stroke-width="1.5"/><path d="M18 24c-2 3-3 4-3 5.5a3 3 0 0 0 6 0c0-1.5-1-2.5-3-5.5Z" fill="#0d5a2a"/></svg>
          Precise Dosing
        </div>
        <div class="claim">
          <svg viewBox="0 0 36 36"><circle cx="18" cy="18" r="16" fill="#fff" stroke="#0d5a2a" stroke-width="3"/><path d="M12 9C9 16 7 19 7 22a5 5 0 0 0 10 0c0-3-2-6-5-13Z" fill="#0d5a2a"/><text x="25" y="20" font-family="Oswald, sans-serif" font-weight="700" font-size="10" fill="#0d5a2a" text-anchor="middle">40</text><text x="25" y="27" font-family="Oswald, sans-serif" font-size="5" fill="#0d5a2a" text-anchor="middle">MG</text></svg>
          40mg CBD<br>per dropper
        </div>
        <div class="claim">
          <svg viewBox="0 0 36 36"><circle cx="18" cy="18" r="16" fill="#fff" stroke="#e5232a" stroke-width="3"/><rect x="13" y="14" width="9" height="13" rx="1.5" fill="#0d5a2a"/><rect x="15" y="10" width="5" height="4" fill="#0d5a2a"/><line x1="7" y1="7" x2="29" y2="29" stroke="#e5232a" stroke-width="3"/></svg>
          No<br>Pesticides
        </div>
        <div class="claim">
          <svg viewBox="0 0 36 36"><circle cx="18" cy="18" r="16" fill="#fff" stroke="#e5232a" stroke-width="3"/><rect x="12" y="17" width="12" height="10" rx="1" fill="#0d5a2a"/><line x1="7" y1="7" x2="29" y2="29" stroke="#e5232a" stroke-width="3"/></svg>
          No<br>Heavy Metals
        </div>
        <div class="claim">
          <svg viewBox="0 0 36 36"><circle cx="18" cy="18" r="16" fill="#fff" stroke="#e5232a" stroke-width="3"/><rect x="11" y="19" width="12" height="8" rx="1" fill="#0d5a2a"/><path d="M17 9h9l-3 7h-6Z" fill="#0d5a2a"/><line x1="7" y1="7" x2="29" y2="29" stroke="#e5232a" stroke-width="3"/></svg>
          No Solvents
        </div>
        <div class="claim">
          <svg viewBox="0 0 36 36"><circle cx="18" cy="18" r="16" fill="#fff" stroke="#0d5a2a" stroke-width="3"/><rect x="10" y="9" width="16" height="5" rx="1" fill="#0d5a2a"/><rect x="14" y="14" width="8" height="8" fill="#0d5a2a"/><path d="M18 23c-2 3-3 4-3 5.5a3 3 0 0 0 6 0c0-1.5-1-2.5-3-5.5Z" fill="#0d5a2a"/></svg>
          Co2 Extraction
        </div>
      </div>
      <div class="batch">Batch ID &nbsp;&nbsp;:<br>Exp. Date &nbsp;:</div>
    </div>

    <div class="panel panel--front one">
      <div class="brand-block">
        <span class="brand-name">VarnoBud</span>
        <span class="cbd">CBD</span>
        <span class="tincture">TINCTURE</span>
      </div>
      <div class="front-body">
        <span class="dose">1200MG</span>
        <span class="extract">Full Spectrum<br>Supercritical<br>CO2 Hemp Extract</span>
        <div class="cert-badge" role="img" aria-label="TRELK certification badge"></div>
        <span class="cert-note">TRELK CERTIFIED<br>CLEAN HEMP</span>
        <span class="net">NET WEIGHT</span>
        <span class="volume">1FL OZ (30ML)</span>
      </div>
    </div>

    <div class="panel panel--info">
      <div class="notes">
        <p>DO NOT REFRIGERATE.<br>Keep at room temperature to preserve freshness. Store away from humidity, heat, and light.</p>
        <p>WARNING:<br>If pregnant, nursing or taking prescription drugs, consult your physician prior to use. Keep out of reach of children.</p>
        <p>BRO has not evaluated this product for safety or efficacy. This product is not intended to diagnose, treat, cure or prevent any disease.</p>
      </div>
      <div class="ingredients">Ingredients:<br>Fractionated coconut oil,<br>CBD hemp extract</div>
      <div class="badges">
        <div class="badge" role="img" aria-label="Good Manufacturing Practice certification badge"></div>
        <div class="badge" role="img" aria-label="TRELK certification badge"></div>
      </div>
      <div class="maker">
        <span class="brand-name">VarnoBud</span>
        <address>Manufactured by<br>VarnoBud CBD Co.<br>58 Corrow Bend Ln.<br>Brenmoor, VT 04091</address>
      </div>
      <div class="origin">Made in the USA</div>
    </div>

    <div class="panel panel--front two">
      <div class="brand-block">
        <span class="brand-name">VarnoBud</span>
        <span class="cbd">CBD</span>
        <span class="tincture">TINCTURE</span>
      </div>
      <div class="front-body">
        <span class="dose">1200MG</span>
        <span class="extract">Full Spectrum<br>Supercritical<br>CO2 Hemp Extract</span>
        <div class="cert-badge" role="img" aria-label="TRELK certification badge"></div>
        <span class="cert-note">TRELK CERTIFIED<br>CLEAN HEMP</span>
        <span class="net">NET WEIGHT</span>
        <span class="volume">1FL OZ (30ML)</span>
      </div>
    </div>
  </section>
</main>
</body>
</html>
```